A picture showing off our Million Dollar Renovation Update at Meadow Falls Splashpark Lodge

Use the uploaded images to develop a picture at least 1366x512 with text saying - Check out our Million Dollar Renovation - I have uploaded alot please use the best to show off . It will go as the hero picture on this website https://meadowfallslodge.example/ - would also to use in social in a "splash" manner to show off updates

Target Market(s)

visitors to our website and past guest

Industry/Entity Type

Hotel

Requirements
Must have
• Check out Our Million Dollar Renovation!
Nice to have
• pictures

```html
<!DOCTYPE html>
<html lang="en">
<head>
<meta charset="utf-8">
<title>Meadow Falls Splashpark Lodge – Million Dollar Renovation Hero Banners</title>
<link href="https://fonts.googleapis.com/css2?family=Lato:ital,wght@0,400;1,400;1,900&display=swap" rel="stylesheet">
<style>
  :root {
    --board: #333333;
    --navy-deep: #1b2a5c;
    --navy-light: #2c4380;
    --yellow: #e5ee00;
    --white: #ffffff;
    --label-grey: #7a7a7a;
    --ink: #1b2a5c;
  }
  html, body {
    margin: 0;
    padding: 0;
    width: 1044px;
    height: 1200px;
    overflow: hidden;
    background: var(--board);
    font-family: "Lato", sans-serif;
  }
  .board { position: relative; width: 1044px; height: 1200px; }

  .hero {
    position: absolute;
    left: 62px;
    width: 921px;
    height: 345px;
    box-shadow: 0 4px 14px rgba(0,0,0,.45);
  }
  .hero svg { position: absolute; inset: 0; display: block; }
  .hero--stacked { top: 109px; }
  .hero--strip { top: 578px; height: 344px; }

  .headline-intro {
    position: absolute;
    left: 30px;
    top: 36px;
    margin: 0;
    font-style: italic;
    font-weight: 400;
    font-size: 42px;
    line-height: 1;
    color: var(--white);
  }
  .headline-big {
    position: absolute;
    left: 28px;
    margin: 0;
    font-style: italic;
    font-weight: 900;
    font-size: 88px;
    line-height: 1;
    letter-spacing: -2px;
    color: var(--yellow);
  }
  .headline-big--million { top: 77px; }
  .headline-big--dollar { top: 150px; }
  .headline-band-text {
    position: absolute;
    left: 24px;
    top: 250px;
    margin: 0;
    font-style: italic;
    font-weight: 900;
    font-size: 58px;
    line-height: 1;
    letter-spacing: -1.5px;
    color: var(--ink);
  }

  .strip-text {
    position: absolute;
    left: 0;
    right: 0;
    top: 266px;
    height: 78px;
    margin: 0;
    display: flex;
    align-items: center;
    justify-content: center;
    font-style: italic;
    font-size: 44px;
    line-height: 1;
    color: var(--white);
    letter-spacing: -0.5px;
    white-space: nowrap;
  }
  .strip-text .accent { color: var(--yellow); font-weight: 900; margin-left: 11px; letter-spacing: -1px; }

  .sample-label {
    position: absolute;
    right: 64px;
    margin: 0;
    font-style: italic;
    font-size: 38px;
    line-height: 1;
    color: var(--label-grey);
  }
  .sample-label--one { top: 494px; }
  .sample-label--two { top: 963px; }

  .spec {
    position: absolute;
    left: 0;
    right: 0;
    top: 1040px;
    margin: 0;
    text-align: center;
    font-style: italic;
    font-size: 40px;
    line-height: 1.25;
    color: var(--white);
  }
</style>
</head>
<body>
<main class="board">

  <section class="hero hero--stacked" aria-label="Hero banner, stacked layout">
    <svg viewBox="0 0 921 345" width="921" height="345">
      <defs>
        <linearGradient id="navyPanel" x1="0" x2="1" y1="0" y2="0">
          <stop offset="0" stop-color="#1b2a5c"/>
          <stop offset="0.6" stop-color="#2c4380"/>
          <stop offset="1" stop-color="#1b2a5c"/>
        </linearGradient>
        <linearGradient id="roomLoft" x1="0" y1="0" x2="0" y2="1">
          <stop offset="0" stop-color="#f2e8d2"/>
          <stop offset="0.35" stop-color="#ead9b6"/>
          <stop offset="0.55" stop-color="#8fc3cf"/>
          <stop offset="0.72" stop-color="#5f5a57"/>
          <stop offset="1" stop-color="#47423f"/>
        </linearGradient>
        <linearGradient id="roomGreen" x1="0" y1="0" x2="0" y2="1">
          <stop offset="0" stop-color="#d8d6cf"/>
          <stop offset="0.18" stop-color="#4e9c55"/>
          <stop offset="0.45" stop-color="#3f7f4a"/>
          <stop offset="0.62" stop-color="#72b09a"/>
          <stop offset="0.8" stop-color="#55504c"/>
          <stop offset="1" stop-color="#45403d"/>
        </linearGradient>
        <linearGradient id="roomLounge" x1="0" y1="0" x2="0" y2="1">
          <stop offset="0" stop-color="#f3ecdd"/>
          <stop offset="0.3" stop-color="#e8dcc2"/>
          <stop offset="0.55" stop-color="#6d5442"/>
          <stop offset="0.72" stop-color="#5a5552"/>
          <stop offset="1" stop-color="#454140"/>
        </linearGradient>
        <linearGradient id="roomHall" x1="0" y1="0" x2="0" y2="1">
          <stop offset="0" stop-color="#efe4cb"/>
          <stop offset="0.4" stop-color="#e6d6b4"/>
          <stop offset="0.7" stop-color="#d9cdb5"/>
          <stop offset="0.85" stop-color="#57524f"/>
          <stop offset="1" stop-color="#46413f"/>
        </linearGradient>
      </defs>
      <rect width="921" height="345" fill="var(--white)"/>
      <polygon points="0,0 470,0 374,345 0,345" fill="url(#navyPanel)"/>
      <polygon points="466,0 478,0 382,345 370,345" fill="var(--yellow)"/>
      <polygon points="0,246 414,246 396,310 0,310" fill="var(--yellow)"/>
      <polygon points="478,0 723,0 676,170 431,170" fill="url(#roomLoft)" role="img" aria-label="Photo: renovated loft suite with king bed, tall window and freestanding tub"/>
      <polygon points="729,0 921,0 921,170 682,170" fill="url(#roomGreen)" role="img" aria-label="Photo: renovated king room with green feature wall and teal bedding"/>
      <polygon points="429,176 668,176 621,345 382,345" fill="url(#roomLounge)" role="img" aria-label="Photo: suite lounge with desk, TV, coffee table and spiral staircase"/>
      <polygon points="674,176 921,176 921,345 627,345" fill="url(#roomHall)" role="img" aria-label="Photo: renovated hallway with window looking over the town"/>
    </svg>
    <p class="headline-intro">Check out our</p>
    <p class="headline-big headline-big--million">MILLION</p>
    <p class="headline-big headline-big--dollar">DOLLAR</p>
    <p class="headline-band-text">RENOVATION</p>
  </section>

  <p class="sample-label sample-label--one">Sample 1</p>

  <section class="hero hero--strip" aria-label="Hero banner, strip layout">
    <svg viewBox="0 0 921 344" width="921" height="344">
      <defs>
        <linearGradient id="bandNavy" x1="0" x2="1" y1="0" y2="0">
          <stop offset="0" stop-color="#1b2a5c"/>
          <stop offset="0.5" stop-color="#2c4380"/>
          <stop offset="1" stop-color="#1b2a5c"/>
        </linearGradient>
        <linearGradient id="stripGreen" x1="0" y1="0" x2="0" y2="1">
          <stop offset="0" stop-color="#d8d6cf"/>
          <stop offset="0.12" stop-color="#4e9c55"/>
          <stop offset="0.42" stop-color="#3f7f4a"/>
          <stop offset="0.6" stop-color="#72b09a"/>
          <stop offset="0.78" stop-color="#55504c"/>
          <stop offset="1" stop-color="#45403d"/>
        </linearGradient>
        <linearGradient id="stripLoft" x1="0" y1="0" x2="0" y2="1">
          <stop offset="0" stop-color="#f2e8d2"/>
          <stop offset="0.4" stop-color="#ead9b6"/>
          <stop offset="0.62" stop-color="#8fc3cf"/>
          <stop offset="0.78" stop-color="#5f5a57"/>
          <stop offset="1" stop-color="#47423f"/>
        </linearGradient>
        <linearGradient id="stripLounge" x1="0" y1="0" x2="0" y2="1">
          <stop offset="0" stop-color="#f3ecdd"/>
          <stop offset="0.4" stop-color="#e8dcc2"/>
          <stop offset="0.65" stop-color="#6d5442"/>
          <stop offset="0.8" stop-color="#5a5552"/>
          <stop offset="1" stop-color="#454140"/>
        </linearGradient>
      </defs>
      <rect width="921" height="344" fill="var(--white)"/>
      <polygon points="0,0 323,0 251,260 0,260" fill="url(#stripGreen)" role="img" aria-label="Photo: renovated king room with green feature wall and teal bedding"/>
      <polygon points="330,0 659,0 591,260 258,260" fill="url(#stripLoft)" role="img" aria-label="Photo: renovated loft suite with king bed, tall window and freestanding tub"/>
      <polygon points="666,0 921,0 921,260 598,260" fill="url(#stripLounge)" role="img" aria-label="Photo: suite lounge with spiral staircase, desk, TV and coffee table"/>
      <rect x="0" y="266" width="921" height="78" fill="url(#bandNavy)"/>
    </svg>
    <p class="strip-text">Check out our<span class="accent">MILLION DOLLAR RENOVATION</span></p>
  </section>

  <p class="sample-label sample-label--two">Sample 2</p>

  <p class="spec">1366x512<br>Our Million Dollar Renovation</p>

</main>
</body>
</html>
```